Modernes Briefpapier für Steuerberater
Zielgruppe
Ich bin Steuerbertaer und brauche ein modernes Briefpapier, was elegant, aber seriös daherkommt.
Aufgabenstellung
Ein Briefpapier mit meinem Logo. Gerne in die Richtung des anderen angehängten Bildes vom Design her.

```html
<!DOCTYPE html>
<html lang="de">
<head>
<meta charset="utf-8">
<title>Kellwitz Steuerberatung – Geschäftsausstattung</title>
<link rel="stylesheet" href="https://fonts.googleapis.com/css2?family=Montserrat:wght@600&family=Open+Sans:wght@400;600&display=swap">
<style>
  :root {
    --brand-blue: #29a8e0;
    --brand-grey: #6d6e70;
    --text-dark: #3a3a3a;
    --paper: #ffffff;
    --stage: #eef1f4;
    --window-fill: #f7f7f7;
    --window-edge: #b5b5b5;
    --photo-light: #f4f7fa;
    --photo-mid: #d9e3ec;
    --photo-deep: #2c3f63;
  }
  * { box-sizing: border-box; margin: 0; padding: 0; }
  html, body { width: 1200px; height: 1077px; overflow: hidden; }
  body { background: var(--stage); position: relative; font-family: "Open Sans", Arial, sans-serif; }

  .wordmark { display: flex; align-items: center; gap: 10px; }
  .wordmark__square { width: 40px; height: 40px; border: 2px solid var(--brand-blue); }
  .wordmark__name {
    font-family: "Montserrat", Arial, sans-serif; font-weight: 600;
    font-size: 14px; letter-spacing: 0.3px; color: var(--brand-grey); white-space: nowrap;
  }

  .card { position: absolute; width: 375px; height: 245px; background: var(--paper); overflow: hidden; }
  .card--front { left: 160px; top: 175px; }
  .card--front .wordmark { position: absolute; left: 48px; top: 65px; }
  .card__strip { position: absolute; left: 0; right: 0; bottom: 0; height: 6px; background: var(--brand-blue); }
  .card__contact {
    position: absolute; left: 52px; top: 170px; font-size: 9px; line-height: 12.5px;
    color: var(--text-dark); font-weight: 600;
  }
  .card__contact--right { left: 182px; top: 182.5px; }
  .card__contact a { color: var(--brand-blue); text-decoration: none; }

  .card--back { left: 585px; top: 175px; }
  .card__photo {
    position: absolute; inset: 0;
    background:
      radial-gradient(ellipse 90px 130px at 95px 185px, var(--photo-deep) 0%, var(--photo-deep) 55%, transparent 75%),
      linear-gradient(180deg, var(--photo-light) 0%, var(--photo-mid) 60%, var(--photo-light) 100%);
  }
  .card--back .wordmark { position: absolute; right: 18px; top: 36px; gap: 8px; }
  .card--back .wordmark__square { width: 28px; height: 28px; }
  .card--back .wordmark__name { font-size: 11px; }
  .card__person { position: absolute; right: 22px; top: 170px; text-align: right; }
  .card__name { font-size: 15px; font-weight: 600; color: var(--brand-blue); }
  .card__title { font-size: 10px; line-height: 13px; color: var(--text-dark); font-weight: 600; }

  .envelope { position: absolute; left: 147px; top: 450px; width: 850px; height: 435px; background: var(--paper); overflow: hidden; }
  .envelope .wordmark { position: absolute; left: 78px; top: 90px; gap: 12px; }
  .envelope .wordmark__square { width: 42px; height: 42px; }
  .envelope .wordmark__name { font-size: 15px; }
  .envelope__window {
    position: absolute; left: 75px; top: 193px; width: 352px; height: 177px;
    border-radius: 30px; background: var(--window-fill);
    border: 3px solid var(--window-edge); box-shadow: inset 0 0 10px rgba(0,0,0,0.15);
  }
  .envelope__url { position: absolute; left: 134px; top: 388px; font-size: 11px; color: var(--brand-blue); }
  .envelope__band { position: absolute; left: 0; bottom: 0; width: 850px; height: 30px; }
</style>
</head>
<body>

  <section class="card card--front" aria-label="Visitenkarte Vorderseite">
    <div class="wordmark">
      <span class="wordmark__square"></span>
      <span class="wordmark__name">KELLWITZ STEUERBERATUNG</span>
    </div>
    <p class="card__contact">
      Lindenweg 12|35390 Gießen<br>
      Telefon: 0641- 123 456 70<br>
      Mobil&nbsp; : 0170 - 1234567
    </p>
    <p class="card__contact card__contact--right">
      info@steuerberatung-kellwitz.de<br>
      <a>www.kellwitz-steuerberatung.de</a>
    </p>
    <div class="card__strip"></div>
  </section>

  <section class="card card--back" aria-label="Visitenkarte Rückseite">
    <div class="card__photo" role="img" aria-label="Porträtfoto des Steuerberaters im Anzug vor einem hellen, lichtdurchfluteten Raum"></div>
    <div class="wordmark">
      <span class="wordmark__square"></span>
      <span class="wordmark__name">KELLWITZ STEUERBERATUNG</span>
    </div>
    <div class="card__person">
      <p class="card__name">Jonas Kellwitz</p>
      <p class="card__title">Dipl.-Betriebswirt (FH)<br>Steuerberater</p>
    </div>
  </section>

  <section class="envelope" aria-label="Briefumschlag mit Fenster">
    <div class="wordmark">
      <span class="wordmark__square"></span>
      <span class="wordmark__name">KELLWITZ STEUERBERATUNG</span>
    </div>
    <div class="envelope__window"></div>
    <p class="envelope__url">www.kellwitz-steuerberatung.de</p>
    <svg class="envelope__band" viewBox="0 0 850 30" aria-hidden="true">
      <rect x="0" y="24" width="850" height="6" fill="var(--brand-blue)"/>
      <path d="M495 30 C515 12 530 4 560 4 L850 4 L850 30 Z" fill="var(--brand-blue)"/>
    </svg>
  </section>

</body>
</html>
```